KW Depot ltd*

I need a full website designed for for a 10,000m2 strorage facity which specialize in heavy commercial storage

it needs to be in english please

Target Market(s)

Comercial sector

Industry/Entity Type

Construction Company

Logo Text

KW

Coding

Coded - Design and coding required

Number of Pages Required

1 page

Font styles to use
Sans Serif

Colors
ec1f27
ffffff

Requirements
Must have
• Tel 0064 219486375
• email- mark@kwdepot.co.nz
Nice to have
• We specilize in large items with the facilty have 3 15tonne Gantry cranes and heavy mobile lifting equipment we can store items up to 20 tonne and we are fully covered and secure.
• square meter rates from 20m2 to 10,000 m2

```html
<!DOCTYPE html>
<html lang="en">
<head>
<meta charset="utf-8">
<title>KW Depot ltd – Heavy Commercial Storage</title>
<link rel="stylesheet" href="https://fonts.googleapis.com/css2?family=Ubuntu:wght@500;700&family=Source+Sans+3:ital,wght@0,400;0,600;0,700;1,400&display=swap">
<style>
:root{
  --red:#ec1f27;
  --dark:#1f1f26;
  --ink:#2b2b2b;
  --grey:#ededed;
  --white:#ffffff;
  --line:#d9d9d9;
}
*{box-sizing:border-box;margin:0;padding:0}
html,body{width:1200px;height:2384px;overflow:hidden;background:var(--white)}
body{position:relative;font-family:"Source Sans 3",sans-serif;color:var(--ink)}
.abs{position:absolute}
.brand{font-family:"Ubuntu",sans-serif;font-weight:700;color:var(--red);display:flex;align-items:center;gap:8px}
.brand .dot{width:14px;height:14px;border-radius:50%;background:var(--red)}
.info{display:flex;gap:9px;font-size:12px;line-height:16px}
.info .ic{width:30px;height:30px;border:1.5px solid var(--red);border-radius:50%;display:flex;align-items:center;justify-content:center;flex:none}
.info b{font-weight:700;display:block}
.nav{left:0;top:80px;width:1200px;height:42px;background:var(--dark)}
.nav a{position:absolute;top:0;height:42px;line-height:42px;color:var(--white);font-size:14px;text-decoration:none}
.nav .home{left:73px;width:81px;text-align:center;background:var(--red);border-bottom:3px solid var(--white)}
.quote{position:absolute;left:968px;top:0;width:160px;height:42px;background:var(--red);clip-path:polygon(10px 0,100% 0,calc(100% - 10px) 100%,0 100%);color:var(--white);font-size:14px;line-height:42px;text-align:center}
.photo{position:absolute}
.hero{left:0;top:122px;width:1200px;height:351px;background:linear-gradient(180deg,#8a8f8c 0%,#b8a27a 40%,#9aa4b0 75%,#c3c9d1 100%)}
.hero-card{left:418px;top:191px;width:299px;height:132px}
.hero-card .top{height:101px;background:#f2f2f2;padding:14px 23px;font-family:"Ubuntu",sans-serif;color:#222}
.hero-card .big{font-size:38px;line-height:40px;font-weight:500}
.hero-card .small{font-size:24px;line-height:30px;font-weight:500}
.hero-card .more{height:31px;background:var(--red);color:var(--white);font-size:15px;text-align:right;padding:5px 20px}
.dots{left:573px;top:429px;display:flex;gap:6px}
.dots span{width:8px;height:8px;border-radius:50%;background:var(--white)}
.dots span.on{background:var(--red);box-shadow:0 0 0 2px var(--white)}
h1.welcome{left:74px;top:516px;font-family:"Ubuntu",sans-serif;font-size:30px;font-weight:700;color:var(--dark)}
.lede{left:74px;top:568px;width:679px;font-size:15.5px;line-height:23px;font-style:italic;color:var(--red);text-align:justify;z-index:2}
.body-copy{left:74px;top:650px;width:502px;font-size:15.5px;line-height:26.4px;text-align:justify}
.welcome-img{left:597px;top:513px;width:530px;height:287px;background:linear-gradient(160deg,#5d6c88 0%,#c8a04a 45%,#d4d2c6 75%,#b9b6aa 100%)}
.notch{left:597px;top:560px;width:173px;height:81px;background:var(--white)}
.band{left:0;top:855px;width:1200px;height:351px;background:linear-gradient(100deg,#7a5a3a 0%,#e09a3e 35%,#d98a2f 55%,#4e4a48 80%,#7d6f66 100%)}
.panel{left:662px;top:891px;width:465px;height:347px}
.panel .head{height:56px;background:var(--dark);color:var(--white);font-family:"Ubuntu",sans-serif;font-size:30px;font-weight:500;padding:12px 21px}
.panel .text{height:259px;background:var(--grey);padding:13px 10px 0 20px;font-size:15px;line-height:26.3px;letter-spacing:-.2px}
.panel .text i{display:block;line-height:21px;margin-bottom:20px}
.panel .bar{height:32px;background:var(--red);color:var(--white);display:flex;justify-content:space-between;align-items:center;padding:0 16px 0 20px}
.panel .bar .l{font-size:16px}
.panel .bar .r{font-size:14px}
.services-h{left:0;top:1266px;width:1200px;text-align:center;font-size:26px;font-weight:700;letter-spacing:-.5px}
.services-s{left:0;top:1306px;width:1200px;text-align:center;font-size:15px}
.card-img{top:1355px;width:410px;height:228px}
.card-label{top:1570px;width:206px;height:38px;background:var(--dark);color:var(--white);font-family:"Ubuntu",sans-serif;font-size:18px;font-weight:500;text-align:center;line-height:38px}
.card-text{top:1622px;width:415px;font-size:14.5px;line-height:21.5px}
.contact-band{left:0;top:1728px;width:1200px;height:413px;background:linear-gradient(90deg,#c9cfdc 0%,#aeb4c4 25%,#9b7a55 45%,#6b5440 70%,#4b3a2d 100%)}
.form{left:732px;top:1765px;width:357px}
.form h2{font-size:22px;font-weight:700;color:var(--white);letter-spacing:-.4px}
.form p{font-size:14px;color:var(--white);margin:2px 0 8px}
.field{height:35px;background:var(--white);margin-bottom:8px;font-size:13.5px;color:#666;padding:8px 16px}
.field.msg{height:91px}
.submit{width:97px;height:32px;background:var(--red);color:var(--white);font-size:13px;font-weight:700;line-height:32px;padding-left:21px}
.footer-rule{top:2185px;width:1px;height:128px;background:var(--line)}
.f-h{font-size:15px;font-weight:700}
.f-list{font-size:14px;line-height:23.8px}
.f-row{display:flex;gap:12px;align-items:flex-start;font-size:14px;line-height:23.8px}
.f-row svg{flex:none;margin-top:5px}
.social{left:932px;top:2208px;display:flex;gap:6px}
.social span{width:31px;height:31px;border-radius:50%;background:var(--red);box-shadow:0 0 0 2px #f6c2c4}
</style>
</head>
<body>

<header>
  <div class="abs brand" style="left:73px;top:22px;font-size:30px"><span class="dot"></span>KW Depot</div>
  <div class="abs info" style="left:611px;top:15px">
    <span class="ic"><svg width="14" height="14" viewBox="0 0 14 14"><path d="M3 1h8M3 13h8M4 1c0 4 6 4 6 6s-6 2-6 6M10 1c0 4-6 4-6 6s6 2 6 6" stroke="#ec1f27" fill="none" stroke-width="1.3"/></svg></span>
    <div><b>Opening Hours</b>Monday-Thursday: 7am-3.30pm<br>Friday: 7am-3pm</div>
  </div>
  <div class="abs info" style="left:837px;top:15px">
    <span class="ic"><svg width="14" height="12" viewBox="0 0 14 12"><rect x="1" y="1" width="12" height="10" fill="#ec1f27"/><path d="M1 1l6 5 6-5" stroke="#fff" fill="none"/></svg></span>
    <div><b>Mail Us</b>mark@kwdepot.co.nz</div>
  </div>
  <div class="abs info" style="left:1014px;top:15px">
    <span class="ic"><svg width="14" height="14" viewBox="0 0 14 14"><path d="M3 1l3 3-2 2c1 2 2 3 4 4l2-2 3 3-2 2C6 13 1 8 1 3z" fill="none" stroke="#ec1f27" stroke-width="1.2"/></svg></span>
    <div><b>Call Us</b>0064 219486375<br>0064 219486376</div>
  </div>
</header>

<nav class="abs nav">
  <a class="home">Home</a>
  <a style="left:182px">Warehousing</a>
  <a style="left:300px">Vanning / Devanning</a>
  <a style="left:458px">Picking / Packing</a>
  <a style="left:600px">Contact Us</a>
  <div class="quote">GET A QUOTE</div>
</nav>

<section>
  <div class="photo hero" role="img" aria-label="Heavy storage hall with gantry cranes and two workers in hi-vis vests"></div>
  <div class="abs hero-card">
    <div class="top"><div class="big">10,000 m<sup style="font-size:20px">2</sup> of</div><div class="small">Storage Space</div></div>
    <div class="more">More Info ›</div>
  </div>
  <div class="abs dots"><span class="on"></span><span></span><span></span><span></span></div>
</section>

<section>
  <h1 class="abs welcome">Welcome to KW Depot</h1>
  <div class="photo welcome-img" role="img" aria-label="Heavy mobile lifting equipment in a large bright warehouse hall"></div>
  <div class="abs notch"></div>
  <p class="abs lede">Based in Ashby, Fernvale, we offer heavy commercial storage for large items, with three 15 tonne gantry cranes and heavy mobile lifting equipment on site, storing items up to 20 tonne, fully covered and secure.</p>
  <p class="abs body-copy">KW Depot offers a modern, secure commercial storage facility of 10,000 m² for handling, storage and distribution of heavy and oversized goods. We work with commercial businesses handling a wide range of products and have the expertise and equipment on site for loading and offloading tankers and sea going containers as well as picking and packing, and palletising stock.</p>
</section>

<section>
  <div class="photo band" role="img" aria-label="Open shipping container filled with cardboard boxes beside a keyboard and globe"></div>
  <div class="abs panel">
    <div class="head">Warehousing</div>
    <div class="text"><i>Fully covered &amp; secure / 3 × 15 tonne gantry cranes / Items up to 20 tonne / Rates from 20 m² to 10,000 m²</i>KW Depot offers square metre rates from 20 m² up to 10,000 m² of covered storage. Our three 15 tonne gantry cranes and heavy mobile lifting equipment let us handle large items up to 20 tonne, with the expertise on site for loading and offloading tankers, and sea going containers, as well as picking packing and palletising goods.</div>
    <div class="bar"><span class="l">Enquire Now ›</span><span class="r">Reach Us @ 0064 219486375</span></div>
  </div>
</section>

<section>
  <h2 class="abs services-h">WE PROVIDE WORLD`S BEST SERVICE</h2>
  <p class="abs services-s">We are handling best service in Vanning/Devanning and Picking &amp; Packing</p>
  <div class="photo card-img" style="left:183px;background:linear-gradient(90deg,#c9ccd0 0%,#3d3f44 30%,#6d6f73 55%,#c9a987 75%,#b99878 100%)" role="img" aria-label="Open container doors with shrink-wrapped pallets of boxes"></div>
  <div class="abs card-label" style="left:183px">Vanning / Devanning</div>
  <p class="abs card-text" style="left:183px">KW Depot offer a professional vanning and devanning service for loading and offloading sea going containers 40’ 20’ plus high cube containers.</p>
  <div class="photo card-img" style="left:639px;background:linear-gradient(90deg,#d9b27c 0%,#c89a5e 40%,#d4b22a 65%,#5b5e63 100%)" role="img" aria-label="Robotic arm stacking cardboard boxes on a pallet"></div>
  <div class="abs card-label" style="left:639px">Picking / Packing</div>
  <p class="abs card-text" style="left:639px">KW Depot offer a dedicated Pick, Pack and distribute service allowing the quick and easy fulfilment of orders for our customer base.</p>
</section>

<section>
  <div class="photo contact-band" role="img" aria-label="Worker with a clipboard checking cardboard boxes"></div>
  <form class="abs form">
    <h2>GET IN TOUCH</h2>
    <p>Please fill the below fields to reach us.</p>
    <div class="field">Enter Name</div>
    <div class="field">Enter Email Address</div>
    <div class="field">Enter Phone Number</div>
    <div class="field msg">Message</div>
    <div class="submit">SUBMIT ›</div>
  </form>
</section>

<footer>
  <div class="abs brand" style="left:73px;top:2180px;font-size:26px"><span class="dot"></span>KW Depot</div>
  <p class="abs" style="left:74px;top:2240px;font-size:13.5px">kwdepot © 2020. All rights reserved</p>
  <div class="abs footer-rule" style="left:315px"></div>
  <div class="abs footer-rule" style="left:526px"></div>
  <div class="abs footer-rule" style="left:877px"></div>
  <div class="abs" style="left:362px;top:2176px">
    <div class="f-h">Quick Links</div>
    <div class="f-list">Home<br>Warehousing<br>Vanning/Devanning<br>Picking &amp; Packing<br>Contact Us</div>
  </div>
  <div class="abs" style="left:575px;top:2176px;width:300px">
    <div class="f-h" style="margin-left:3px">Contact</div>
    <div class="f-row"><svg width="10" height="13" viewBox="0 0 10 13"><path d="M5 0a5 5 0 0 1 5 5c0 3-5 8-5 8S0 8 0 5a5 5 0 0 1 5-5z" fill="#ec1f27"/><circle cx="5" cy="5" r="2" fill="#fff"/></svg><span>18/20 Kestrel Road, Fernvale Industrial<br>Estate, Ashby, FV3 2KD</span></div>
    <div class="f-row"><svg width="12" height="12" viewBox="0 0 14 14"><path d="M3 1l3 3-2 2c1 2 2 3 4 4l2-2 3 3-2 2C6 13 1 8 1 3z" fill="#ec1f27"/></svg><span>0064 219486375</span></div>
    <div class="f-row"><svg width="14" height="12" viewBox="0 0 14 12"><rect x="1" y="5" width="12" height="6" rx="1" fill="#ec1f27"/><path d="M1 4c2-3 10-3 12 0" stroke="#ec1f27" stroke-width="2" fill="none"/></svg><span>0064 219486376</span></div>
    <div class="f-row"><svg width="14" height="13" viewBox="0 0 14 13"><rect x="1" y="4" width="12" height="9" fill="#ec1f27"/><rect x="4" y="0" width="6" height="5" fill="none" stroke="#ec1f27"/></svg><span>0064 219486377</span></div>
  </div>
  <div class="abs f-h" style="left:936px;top:2176px">Follow Us</div>
  <div class="abs social"><span></span><span></span><span></span></div>
</footer>

</body>
</html>
```